New Business Card for Software Company

We are looking at rebranding a 10 year old company that specializes in PDF and DWF solutions for Architects and Engineers. We will attach the new company logo that we are going with so you can work with that and complimentary colors.
The sample information we would like on the business card is:
Gerald Pembrook
Vice President
4173 W. Tillman Avenue. STE 306
PMB#417
Mesa, AZ 85316
866-392-7154 US Toll Free
123-581-3064 Cell
gpembrook@vextrolan.com
The old tag line that we had on the business cars was.
Providing Industrial Strength PDF and DWF Solutions to the Global CAD Marketplace.
If you have an idea for a better tag line we are open to that also.
Updates
We would like to thank all of the Designers for their wonderful work. We apologize that we will not have the time to provide feedback to everyone. There is just so many innovative and professional designs that you have all created making our decision even harder.
Target Market(s)
Architects and Engineers
Industry/Entity Type
Business
Look and feel
Each slider illustrates characteristics of the customer's brand and the style your logo design should communicate.

```html
<!DOCTYPE html>
<html lang="en">
<head>
<meta charset="utf-8">
<title>Vextrolan Business Cards</title>
<link href="https://fonts.googleapis.com/css2?family=Open+Sans:wght@400;600&display=swap" rel="stylesheet">
<style>
  :root {
    --page: #ffffff;
    --card: #1e1e1e;
    --text: #c9c9c9;
    --name: #d6d6d6;
    --tagline: #e8e8e8;
    --brand: #f26a1b;
  }
  html, body {
    margin: 0;
    padding: 0;
    background: var(--page);
    overflow: hidden;
  }
  .sheet {
    position: relative;
    width: 743px;
    height: 1200px;
    font-family: "Open Sans", Arial, sans-serif;
  }
  .card {
    position: absolute;
    width: 334px;
    height: 577px;
    background: var(--card);
    box-sizing: border-box;
  }
  .card--front-a { left: 0; top: 0; }
  .card--back-a  { left: 409px; top: 0; }
  .card--front-b { left: 0; top: 611px; height: 589px; }
  .card--back-b  { left: 409px; top: 611px; height: 589px; }

  .contact {
    position: absolute;
    left: 23px;
    top: 26px;
    color: var(--text);
    font-size: 15px;
    line-height: 22px;
  }
  .contact__name {
    margin: 0;
    color: var(--name);
    font-size: 22px;
    line-height: 28px;
    font-weight: 600;
  }
  .contact__title { margin: 0 0 26px; }
  .contact__address,
  .contact__phones { margin: 0 0 24px; }
  .contact__email { margin: 0; }

  .tagline {
    position: absolute;
    left: 22px;
    top: 14px;
    margin: 0;
    width: 140px;
    color: var(--tagline);
    font-size: 15px;
    line-height: 24px;
  }

  .brand {
    position: absolute;
    right: 18px;
    bottom: 22px;
    display: flex;
    align-items: center;
    gap: 8px;
    color: var(--brand);
    font-size: 26px;
    font-weight: 600;
    letter-spacing: -0.3px;
  }
  .brand__dot {
    width: 26px;
    height: 26px;
    border-radius: 50%;
    background: var(--brand);
  }

  .brand-decoration {
    position: absolute;
    left: 30px;
    top: 170px;
    width: 290px;
    height: 320px;
  }
</style>
</head>
<body>
<main class="sheet">

  <section class="card card--front-a">
    <div class="contact">
      <p class="contact__name">Gerald Pembrook</p>
      <p class="contact__title">Vice President</p>
      <p class="contact__address">4173 W. Tillman Avenue. STE 306<br>PMB#417<br>Mesa, AZ 85316</p>
      <p class="contact__phones">866-392-7154 US Toll Free<br>123-581-3064 Cell</p>
      <p class="contact__email">gpembrook@vextrolan.com</p>
    </div>
    <div class="brand"><span class="brand__dot"></span>Vextrolan</div>
  </section>

  <section class="card card--back-a">
    <p class="tagline">Providing PDF and DWF solutions for Architects and Engineers - Worldwide.</p>
    <div class="brand"><span class="brand__dot"></span>Vextrolan</div>
  </section>

  <section class="card card--front-b">
    <div class="contact">
      <p class="contact__name">Gerald Pembrook</p>
      <p class="contact__title">Vice President</p>
      <p class="contact__address">4173 W. Tillman Avenue. STE 306<br>PMB#417<br>Mesa, AZ 85316</p>
      <p class="contact__phones">866-392-7154 US Toll Free<br>123-581-3064 Cell</p>
      <p class="contact__email">gpembrook@vextrolan.com</p>
    </div>
    <div class="brand"><span class="brand__dot"></span>Vextrolan</div>
  </section>

  <section class="card card--back-b">
    <p class="tagline">Providing PDF and DWF solutions for Architects and Engineers - Worldwide.</p>
    <svg class="brand-decoration" role="img" aria-label="Large glossy black brand emblem decoration" viewBox="0 0 290 320">
      <defs>
        <radialGradient id="emblemTone" cx="45%" cy="40%" r="60%">
          <stop offset="0%" stop-color="#6a6a6a"/>
          <stop offset="55%" stop-color="#202020"/>
          <stop offset="100%" stop-color="#1e1e1e" stop-opacity="0"/>
        </radialGradient>
      </defs>
      <rect x="0" y="0" width="290" height="320" rx="40" fill="url(#emblemTone)"/>
    </svg>
    <div class="brand"><span class="brand__dot"></span>Vextrolan</div>
  </section>

</main>
</body>
</html>
```